Bright Oak Collective needs updated website.

Our current website was designed on wix.com. (www.brightoakcollective.com).
We would like something a little more customized for what our company offers. Bright Oak Collective is a company specializing in connecting consumers with trustworthy and affordable service professionals. We need the website to be approachable and easy to use, while conveying our "Bright Oak" reputation.
Updates
Project Deadline Extended
Reason: Our project is now guaranteed. Please send your ideas. Thank you!
Target Market(s)
Homeowners
Industry/Entity Type
It Company
Look and feel
Each slider illustrates characteristics of the customer's brand and the style your logo design should communicate.

```html
<!DOCTYPE html>
<html lang="en">
<head>
<meta charset="utf-8">
<title>Bright Oak Collective</title>
<link href="https://fonts.googleapis.com/css2?family=Open+Sans:wght@400;600;700&display=swap" rel="stylesheet">
<style>
:root{
  --orange:#f26b1d;
  --orange-light:#f8a23a;
  --orange-dark:#e9541a;
  --ink:#222;
  --text:#8c8c8c;
  --rule:#bdbdbd;
  --frame:#e6e6e6;
  --white:#fff;
}
*{margin:0;padding:0;box-sizing:border-box}
html,body{width:843px;height:1200px;overflow:hidden;background:var(--white)}
body{position:relative;font-family:"Open Sans",Arial,sans-serif;color:var(--text)}
.abs{position:absolute}
.main-nav{left:0;top:0;width:843px;height:47px;background:linear-gradient(var(--orange-light),var(--orange) 55%,var(--orange-dark));display:flex}
.main-nav a{color:var(--white);font-weight:700;font-size:14px;text-decoration:none;display:flex;align-items:center;justify-content:center;height:47px;border-right:1px solid rgba(255,255,255,.55)}
.main-nav a:last-child{border-right:none;flex:1}
.brand{left:15px;top:66px;display:flex;align-items:center;gap:10px}
.brand-mark{width:60px;height:60px;border-radius:50%;background:var(--orange)}
.brand-name{font-size:26px;font-weight:700;color:#5a5a5a;line-height:1}
.hotline{right:22px;top:72px;font-size:17px;color:var(--ink)}
.hero-title{left:100px;top:216px;font-size:23px;color:var(--orange);font-weight:400}
.hero-copy{left:100px;top:259px;width:355px;font-size:10.5px;line-height:18.5px}
.btn{display:flex;align-items:center;justify-content:center;background:linear-gradient(#555,#111);color:var(--white);font-size:12px;font-weight:600;border-radius:5px;text-decoration:none}
.hero-btn{left:100px;top:383px;width:93px;height:28px}
.hero-photo{left:473px;top:118px;width:340px;height:330px;background:radial-gradient(ellipse at 55% 45%,#f1c9b4,#e8d6cc 45%,#fff 72%)}
.rule{left:0;width:843px;height:1px;background:var(--rule)}
.heading{font-size:16px;color:var(--ink);font-weight:400}
.frame{border:5px solid var(--frame);background:var(--white);padding:2px}
.frame div{width:100%;height:100%}
.copy{font-size:10.5px;line-height:18px}
.copy p+p{margin-top:16px}
.network-list{left:578px;top:747px;list-style:none;font-size:10.5px}
.network-list li{height:28px;display:flex;align-items:center;gap:10px}
.network-list svg{width:8px;height:9px}
.network-list .note{display:block;line-height:28px;padding-left:18px;margin-top:0}
.footer-links{left:31px;top:1134px;font-size:10px;font-weight:600;color:#555}
.footer-band{left:0;top:1163px;width:843px;height:37px;background:linear-gradient(var(--orange-light),var(--orange) 55%,var(--orange-dark))}
.copyright{left:31px;top:1174px;font-size:10px;color:var(--white)}
.social{left:663px;top:1168px;display:flex;gap:6px}
.social span{width:27px;height:27px;background:linear-gradient(#f4f4f4,#cfcfcf);border-radius:3px}
</style>
</head>
<body>
<nav class="main-nav abs">
  <a href="#" style="width:95px">Home</a>
  <a href="#" style="width:112px">About Us</a>
  <a href="#" style="width:126px">Network</a>
  <a href="#" style="width:154px">Services</a>
  <a href="#" style="width:127px">Vision</a>
  <a href="#" style="width:113px">Blog</a>
  <a href="#">Contact Us</a>
</nav>

<div class="brand abs"><span class="brand-mark"></span><span class="brand-name">Bright Oak Collective</span></div>
<div class="hotline abs">24/7 SERVICE: 1-555-210-4476</div>

<h1 class="hero-title abs">YOU CAN COUNT ON US</h1>
<p class="hero-copy abs">Donec quam felis, ultricies nec, pellentesque eu, pretium quis, sem. Nulla consequat massa quis enim. Donec pede justo, fringilla vel, aliquet nec, vulputate eget, arcu. In enim justo, rhoncus ut, imperdiet a, venenatis vitae, justo. Nullam dictum felis eu pede mollis pretium. Donec quam felis, ultricies nec, pellentesque eu, pretium quis, sem.</p>
<a class="btn hero-btn abs" href="#">View More</a>
<div class="hero-photo abs" role="img" aria-label="Smiling customer service agent wearing a headset"></div>
<div class="rule abs" style="top:448px"></div>

<h2 class="heading abs" style="left:30px;top:470px">WELCOME</h2>
<div class="frame abs" style="left:31px;top:508px;width:227px;height:149px"><div role="img" aria-label="Team of business professionals standing together" style="background:linear-gradient(90deg,#cfc7c0,#3a3a3a 45%,#b9c4cf 75%,#eee)"></div></div>
<div class="copy abs" style="left:287px;top:501px;width:515px">
  <p>Donec quam felis, ultricies nec, pellentesque eu, pretium quis, sem. Nulla consequat massa quis enim. Donec pede justo, fringilla vel, aliquet nec, vulputate eget, arcu. In enim justo, rhoncus ut, imperdiet a, venenatis vitae, justo. Nullam dictum felis eu pede mollis pretium. Donec quam felis, ultricies nec, pellentesque eu, pretium quis, sem. Nulla consequat massa quis enim. Donec pede justo, fringilla vel, aliquet nec, vulputate eget, arcu. In enim justo, rhoncus ut, imperdiet a, ve, rs, sem. Nulla consequat massa quis enim.</p>
  <p>Donec pede justo, fringilla vel, aliquet nec, vulputate eget, arcu. In enim justo, rhoncus ut, imperdiet a, venenatis vitae, justo. Nullam dictum felis eu pede mollis pretium.</p>
</div>
<div class="rule abs" style="top:690px"></div>

<h2 class="heading abs" style="left:30px;top:711px">ABOUT US</h2>
<div class="frame abs" style="left:31px;top:749px;width:227px;height:148px"><div role="img" aria-label="Businesswoman with arms crossed in front of her team" style="background:linear-gradient(90deg,#777,#aaa 40%,#e8cbb5 65%,#222 85%,#fff)"></div></div>
<div class="copy abs" style="left:31px;top:908px;width:230px">
  <p>Donec quam felis, ultricies nec, pellentesque eu, pretium quis, sem. Nulla consequat massa quis enim. Donec pede justo, fringilla vel, aliquet nec, vulputate eget, arcu.</p>
  <p>In enim justo, rhoncus ut, imperdiet a, venenatis vitae, justo. Nullam dictum felis eu pede mollis pretium.</p>
</div>
<a class="btn abs" href="#" style="left:31px;top:1055px;width:92px;height:28px">Register Now</a>

<h2 class="heading abs" style="left:280px;top:711px">OUR VISION</h2>
<div class="frame abs" style="left:284px;top:749px;width:227px;height:148px"><div role="img" aria-label="Modern glass office building under a blue sky" style="background:linear-gradient(160deg,#2f78c8,#4f8fcf 35%,#6a6f78 60%,#c9b9a8)"></div></div>
<div class="copy abs" style="left:284px;top:908px;width:230px">
  <p>Donec quam felis, ultricies nec, pellentesque eu, pretium quis, sem. Nulla consequat massa quis enim. Donec pede justo, fringilla vel, aliquet nec, vulputate eget, arcu.</p>
  <p>In enim justo, rhoncus ut, imperdiet a, venenatis vitae, justo. Nullam dictum felis eu pede mollis pretium.</p>
</div>
<a class="btn abs" href="#" style="left:281px;top:1055px;width:92px;height:28px">Register Now</a>

<h2 class="heading abs" style="left:557px;top:712px">OUR NETWORK</h2>
<ul class="network-list abs">
  <li><svg viewBox="0 0 8 9"><path d="M0 0L8 4.5 0 9z" fill="#111"/></svg>Heating</li>
  <li><svg viewBox="0 0 8 9"><path d="M0 0L8 4.5 0 9z" fill="#111"/></svg>Air Conditioning</li>
  <li><svg viewBox="0 0 8 9"><path d="M0 0L8 4.5 0 9z" fill="#111"/></svg>Automotive Maintenance</li>
  <li><svg viewBox="0 0 8 9"><path d="M0 0L8 4.5 0 9z" fill="#111"/></svg>Automotive Sales</li>
  <li><svg viewBox="0 0 8 9"><path d="M0 0L8 4.5 0 9z" fill="#111"/></svg>Home Repair</li>
  <li><svg viewBox="0 0 8 9"><path d="M0 0L8 4.5 0 9z" fill="#111"/></svg>Painting</li>
  <li><svg viewBox="0 0 8 9"><path d="M0 0L8 4.5 0 9z" fill="#111"/></svg>Chiropractic</li>
  <li><svg viewBox="0 0 8 9"><path d="M0 0L8 4.5 0 9z" fill="#111"/></svg>Carpentry</li>
  <li><svg viewBox="0 0 8 9"><path d="M0 0L8 4.5 0 9z" fill="#111"/></svg>Roofing</li>
  <li><svg viewBox="0 0 8 9"><path d="M0 0L8 4.5 0 9z" fill="#111"/></svg>Don't see what you need,</li>
  <li class="note" style="height:auto">let us know.&nbsp; We will find you the best<br>in the business!!</li>
</ul>

<div class="rule abs" style="top:1117px"></div>
<div class="footer-links abs">Home | About Us | Network | Services | Vision | Blog | Contact Us</div>
<footer class="footer-band abs"></footer>
<div class="copyright abs">Copyright © 2013 Brightoakcollective</div>
<div class="social abs"><span></span><span></span><span></span><span></span><span></span></div>
</body>
</html>
```